Business Card Design

We need a business card design for a new company. We produce and sell fully grown topiary (please Google topiary pictures if you are not familiar with Topiary).We make many different topiary designs and shapes in all sizes. Ranging from cute little table top animal sculptures such as bunnies and swans for the indoors, to big sculptures such as actual size elephants for outdoor gardens and parks. We also make topiary balls, spiral shapes and other attractive geometrical shapes for indoor and outdoor decorations. We want to see designs that reflects the playfulness and ,liveliness and cute characteristics of our products.Please find attached the logo.Thank you

Industry/Entity Type

Business

Contact Information for Business Card

Company Name : Leaf Lark
Slogan : Crafting The World In Green
Tagline: Topiary...and more
Website : www.leaflark.example

Name on Card : Yusuf Tarek Mansour
Title : Founder & CEO
email: yusuf_tarek@leaflark.example

Address : 27 El-Borsaly Street
Ground Floor,Ste.1
El-Haram,Cairo,Egypt

Office Telephone : (02) 35908176
Mobile Number : 01062719048

Requirements
Must have
• The business card must have a white background.

```html
<!DOCTYPE html>
<html lang="en">
<head>
<meta charset="utf-8">
<title>Leaf Lark — Business Card</title>
<link href="https://fonts.googleapis.com/css2?family=Indie+Flower&display=swap" rel="stylesheet">
<style>
  :root {
    --leaf-green: #62bf1c;
    --leaf-green-dark: #3f8f12;
    --paper: #fbfbf9;
    --icon-frame: #6b6b6b;
  }
  html, body {
    margin: 0;
    padding: 0;
    width: 1200px;
    height: 791px;
    overflow: hidden;
    background: var(--paper);
  }
  .card {
    position: relative;
    width: 1200px;
    height: 791px;
    background: var(--paper);
    color: var(--leaf-green);
    font-family: "Indie Flower", cursive;
  }
  .holder {
    position: absolute;
    left: 40px;
    top: 38px;
    margin: 0;
  }
  .holder-name {
    display: block;
    font-size: 40px;
    line-height: 1;
    letter-spacing: 1px;
  }
  .holder-title {
    display: block;
    font-size: 23px;
    line-height: 1.1;
    margin-top: 2px;
  }
  .phones {
    position: absolute;
    left: 954px;
    top: 38px;
    display: flex;
    align-items: center;
    gap: 10px;
  }
  .phones-list {
    font-size: 28px;
    line-height: 0.95;
    letter-spacing: 0.5px;
  }
  .brand {
    position: absolute;
    left: 0;
    top: 300px;
    width: 1200px;
    text-align: center;
  }
  .brand-name {
    display: block;
    font-size: 118px;
    line-height: 1;
    letter-spacing: 2px;
  }
  .brand-slogan {
    display: block;
    font-size: 42px;
    line-height: 1;
    margin-top: 14px;
    margin-left: -10px;
  }
  .tagline {
    position: absolute;
    left: 936px;
    top: 326px;
    font-size: 22px;
    transform: rotate(-14deg);
    transform-origin: left center;
    white-space: nowrap;
  }
  .address {
    position: absolute;
    left: 40px;
    top: 716px;
    display: flex;
    align-items: center;
    gap: 8px;
    font-size: 24px;
  }
  .email {
    position: absolute;
    right: 54px;
    top: 720px;
    font-size: 21px;
    display: flex;
    align-items: center;
  }
  .email-at {
    font-size: 34px;
    margin: 0 2px;
    line-height: 1;
  }
</style>
</head>
<body>
<main class="card">
  <header class="holder">
    <span class="holder-name">Yusuf Tarek Mansour</span>
    <span class="holder-title">Founder &amp; CEO</span>
  </header>

  <div class="phones">
    <svg class="icon-phone" width="28" height="52" viewBox="0 0 28 52" aria-hidden="true">
      <rect x="1" y="1" width="26" height="50" rx="4" fill="var(--icon-frame)"/>
      <rect x="4" y="7" width="20" height="35" fill="var(--leaf-green)"/>
      <circle cx="14" cy="46.5" r="2.2" fill="#ddd"/>
    </svg>
    <div class="phones-list">
      <div class="phone-mobile">01062719048</div>
      <div class="phone-office">(02) 35908176</div>
    </div>
  </div>

  <section class="brand">
    <span class="brand-name">Leaf Lark</span>
    <span class="brand-slogan">crafting the world in green</span>
  </section>

  <div class="tagline">Topiary and more...</div>

  <footer>
    <div class="address">
      <svg class="icon-home" width="42" height="40" viewBox="0 0 42 40" aria-hidden="true">
        <path d="M2 20 L21 3 L40 20" fill="none" stroke="var(--leaf-green)" stroke-width="5" stroke-linejoin="round"/>
        <rect x="8" y="19" width="26" height="19" fill="#f1efe6" stroke="var(--icon-frame)" stroke-width="1.5"/>
        <rect x="12" y="24" width="7" height="14" fill="var(--icon-frame)"/>
        <rect x="23" y="24" width="7" height="7" fill="#9cc7e8" stroke="var(--icon-frame)" stroke-width="1"/>
      </svg>
      <span class="address-text">27 El-Borsaly Street Ground Floor, Ste.1 El Haram, Cairo, Egypt</span>
    </div>
    <div class="email">
      <span>yusuf_tarek</span><span class="email-at">@</span><span>leaflark.example</span>
    </div>
  </footer>
</main>
</body>
</html>
```